New name flyer

We have just changed our business name from kR Property group to Harbour Lantern. We want to distribute a flyer to the local community to inform them of the change. We are a realestate agency which focuses mainly on property management but also sales. We service from Brisbane to the Sunshine coast.

Target Market(s)

Local community

Industry/Entity Type

realestate

Requirements
Must have
• Details of name change
Nice to have
• Servicing area Brisbane and Sunshine Coast, no change in management or services we offer, and will continue pride ourselves on offering a high level of service, with the same team from the Gold to Sunshine Coast.
Should not have
• too much wording.

```html
<!DOCTYPE html>
<html lang="en">
<head>
<meta charset="utf-8">
<title>KR Property Group – New Name Flyer</title>
<link rel="stylesheet" href="https://fonts.googleapis.com/css2?family=Oswald:wght@600&family=Lato:wght@400;700;900&display=swap">
<style>
  :root {
    --navy: #1f3564;
    --gold: #d29e2e;
    --white: #ffffff;
    --stage: #000000;
  }
  * { margin: 0; padding: 0; box-sizing: border-box; }
  html, body {
    width: 1200px; height: 1200px; overflow: hidden;
    background: var(--stage);
    font-family: "Lato", Arial, sans-serif;
  }
  .flyer {
    position: absolute; left: 224px; top: 116px;
    width: 755px; height: 978px;
    background: var(--white); overflow: hidden;
  }
  .flyer-shapes { position: absolute; inset: 0; }
  .old-name {
    position: absolute; left: 334px; top: 35px;
    width: 393px; height: 35px;
    border: 2px solid var(--gold);
    color: var(--white);
    font-size: 19px; letter-spacing: 4px; font-weight: 400;
    display: flex; align-items: center; justify-content: center;
  }
  .change-heading {
    position: absolute; right: 28px; top: 68px;
    font-family: "Oswald", "Arial Narrow", sans-serif;
    font-weight: 600; font-size: 72px; line-height: 1;
    color: var(--gold); letter-spacing: 0.5px;
  }
  .new-name {
    position: absolute; left: 124px; top: 418px;
    font-family: "Lato", Arial, sans-serif;
    font-weight: 900; font-size: 80px; line-height: 78px;
    color: var(--navy); letter-spacing: 2px;
  }
  .tagline {
    position: absolute; left: 0; width: 100%; top: 683px;
    text-align: center; color: var(--navy);
    font-size: 22px; font-weight: 400;
  }
  .services {
    position: absolute; left: 124px; top: 716px;
    width: 507px; height: 46px;
    border: 2px solid var(--gold);
    display: flex; align-items: center; justify-content: center; gap: 12px;
    color: var(--navy); font-size: 27px;
  }
  .services .divider { color: var(--gold); font-weight: 700; }
  .summary {
    position: absolute; left: 0; width: 100%; top: 773px;
    text-align: center; color: var(--navy);
    font-size: 16px; line-height: 22px;
  }
  .contact-address {
    position: absolute; left: 40px; top: 896px;
    color: var(--white); font-size: 17px; line-height: 21px;
  }
  .contact-row { display: flex; align-items: flex-start; gap: 8px; }
  .contact-row svg { flex: none; margin-top: 3px; }
  .contact-row .indent { padding-left: 20px; }
  .contact-web { color: var(--gold); margin-top: 4px; }
  .contact-phone {
    position: absolute; left: 463px; top: 929px;
    display: flex; align-items: center; gap: 16px;
    color: var(--white); font-size: 31px; font-weight: 400;
  }
  .phone-badge {
    width: 38px; height: 38px; background: var(--navy);
    display: flex; align-items: center; justify-content: center;
  }
</style>
</head>
<body>
  <main class="flyer">
    <svg class="flyer-shapes" width="755" height="978" viewBox="0 0 755 978" aria-hidden="true">
      <polygon points="0,0 755,0 755,316 0,62" fill="var(--navy)"/>
      <polygon points="332,174 755,316 755,334 332,190" fill="var(--gold)"/>
      <polygon points="0,878 394,878 424,978 0,978" fill="var(--navy)"/>
      <polygon points="418,914 755,914 755,978 437,978" fill="var(--gold)"/>
    </svg>

    <div class="old-name">KR PROPERTY GROUP</div>
    <h1 class="change-heading">CHANGE NAME TO</h1>

    <h2 class="new-name">HARBOUR<br>LANTERN</h2>

    <p class="tagline">LICENSED REAL ESTATE AGENTS IN BRISBANE</p>
    <div class="services">
      <span>SELL</span><span class="divider">|</span>
      <span>LEASE</span><span class="divider">|</span>
      <span>BUY</span><span class="divider">|</span>
      <span>DEVELOP</span>
    </div>
    <p class="summary">Brisbane northside real estate agency offering sales and<br>property management with high quality service.</p>

    <address class="contact-address">
      <div class="contact-row">
        <svg width="12" height="15" viewBox="0 0 12 15"><path d="M6 0C2.7 0 0 2.6 0 5.8 0 10 6 15 6 15s6-5 6-9.2C12 2.6 9.3 0 6 0zm0 8a2.3 2.3 0 1 1 0-4.6A2.3 2.3 0 0 1 6 8z" fill="var(--gold)"/></svg>
        <span>5/118 Tallow Road</span>
      </div>
      <div class="contact-row"><span class="indent">Northgate Park, Q 4013</span></div>
      <div class="contact-row contact-web">
        <svg width="12" height="12" viewBox="0 0 12 12"><circle cx="6" cy="6" r="5.2" fill="none" stroke="var(--gold)" stroke-width="1.4"/><path d="M1 6h10M6 1c-2.4 2.8-2.4 7.2 0 10M6 1c2.4 2.8 2.4 7.2 0 10" fill="none" stroke="var(--gold)" stroke-width="1.1"/></svg>
        <span>www.krpropertygroup.com.au</span>
      </div>
    </address>

    <div class="contact-phone">
      <span class="phone-badge">
        <svg width="22" height="22" viewBox="0 0 24 24"><path d="M6.6 10.8a15.1 15.1 0 0 0 6.6 6.6l2.2-2.2c.3-.3.7-.4 1-.2 1.1.4 2.3.6 3.6.6.6 0 1 .4 1 1V20c0 .6-.4 1-1 1A17 17 0 0 1 3 4c0-.6.4-1 1-1h3.5c.6 0 1 .4 1 1 0 1.3.2 2.5.6 3.6.1.3 0 .7-.2 1z" fill="var(--white)"/><path d="M15 3a6 6 0 0 1 6 6M15 6.5A2.5 2.5 0 0 1 17.5 9" fill="none" stroke="var(--white)" stroke-width="1.6"/></svg>
      </span>
      <span>07 3000 1842</span>
    </div>
  </main>
</body>
</html>
```